Pine Hollow toothpaste tube design

Design a Pine Hollow tube design for our all natural toothpaste. The toothpaste is 100% natural with a smooth marshmallow consistency. It's unique because it's not pastelike at all. The all natural flavors make the toothpaste taste great. The toothpaste is smooth yet still leaves your mouth feeling squeaky clean. We want to market this as an all natural family toothpaste.

The flavor is Mint. (possibly called "Koda Fern")

We have included our logo (eps & jpg), information that goes on the back of the tube, and the artwork template from the tube supplier for the 4.2oz tube.

We like a vintage earthy retro look and feel but we are not limited to this.

The tubes stand upright as shown in the picture of File 4.
Updates

The finished artwork must include anĀ adobe illustratorĀ file.

Project Deadline Extended

I would like to thank all of the designers for their work on this project. We had a difficult time making a decision since all of the designs were very close to what we expected.

Sincerely,

Rolf

Target Market(s)

The target market is families that desire an all natural toothpaste. We will be stressing the 100% natural and great taste.

Requirements
Must have
• Three colors maximum due to tube manufacture restrictions.

Must have "100% natural" and "fluoride free" on front of tube. A reference to the great taste or flavor is also important.

Must say 4.2 oz on the front of the tube, centered, at the bottom.
Nice to have
• Fun, colorful packaging that will stand out. Go to your local store and stand in front of the tootpaste shelves, give us something different!
Should not have
• We do not want a lot of red or blue because these are predominate colors already in use on toothpaste tubes and boxes.

```html
<!DOCTYPE html>
<html lang="en">
<head>
<meta charset="utf-8">
<title>Pine Hollow Toothpaste – Tube Artwork</title>
<link href="https://fonts.googleapis.com/css2?family=Arvo:wght@700&family=Source+Sans+3:wght@400;600;700&display=swap" rel="stylesheet">
<style>
  :root {
    --backdrop: #f1f1f0;
    --tube-white: #f7f7f5;
    --leaf-green: #4f9a2e;
    --band-light: #8fbf6a;
    --band-dark: #5f9a3c;
    --deep-green: #3f7d25;
    --charcoal: #3d3d3b;
    --cream: #f4f1df;
    --badge-orange: #e9861c;
    --ink: #3a3a38;
  }
  * { box-sizing: border-box; margin: 0; padding: 0; }
  html, body { width: 1200px; height: 900px; overflow: hidden; }
  body {
    background: var(--backdrop);
    font-family: "Source Sans 3", Arial, sans-serif;
    position: relative;
  }
  .tube-panel {
    position: absolute;
    top: 150px;
    width: 260px;
    height: 620px;
    background: var(--tube-white);
    box-shadow: 0 2px 10px rgba(0,0,0,0.08);
    overflow: hidden;
  }
  .front { left: 330px; }
  .back { left: 610px; }

  .brand {
    position: absolute;
    left: 0; right: 0;
    display: flex;
    align-items: center;
    justify-content: center;
    gap: 8px;
    color: var(--leaf-green);
    font-weight: 700;
  }
  .brand-dot {
    width: 16px; height: 16px;
    border-radius: 50%;
    background: var(--leaf-green);
  }
  .front .brand { top: 62px; font-size: 30px; }
  .back .brand { top: 52px; font-size: 24px; }

  .front-lower {
    position: absolute;
    left: 0; right: 0; top: 190px; bottom: 0;
    background: linear-gradient(180deg, #a9cf8c 0%, #6ea94a 45%, #3f7d25 100%);
  }
  .leaf-artwork {
    position: absolute;
    left: 0; right: 0; top: 150px; height: 140px;
    background: radial-gradient(ellipse at 70% 60%, rgba(255,255,255,0.45), rgba(255,255,255,0) 70%);
  }
  .product-name {
    position: absolute;
    left: 0; right: 0; top: 208px;
    text-align: center;
    font-family: "Arvo", Georgia, serif;
    color: var(--charcoal);
    font-size: 30px;
    letter-spacing: 1px;
  }
  .product-type {
    position: absolute;
    left: 0; right: 0; top: 246px;
    text-align: center;
    font-family: "Arvo", Georgia, serif;
    color: var(--charcoal);
    font-size: 13px;
    letter-spacing: 5px;
  }
  .claim-band {
    position: absolute;
    left: 0; right: 0; top: 290px; height: 48px;
    background: var(--band-light);
    color: #fff;
    text-align: center;
    font-size: 11px;
    letter-spacing: 1.5px;
    font-weight: 600;
    line-height: 14px;
    padding-top: 11px;
  }
  .flavor-band {
    position: absolute;
    left: 0; right: 0; top: 338px; height: 70px;
    background: var(--band-dark);
    text-align: center;
    color: var(--cream);
  }
  .flavor-name {
    font-family: "Arvo", Georgia, serif;
    font-size: 22px;
    letter-spacing: 1.5px;
    padding-top: 12px;
  }
  .flavor-label {
    font-size: 11px;
    letter-spacing: 4px;
    margin-top: 2px;
  }
  .new-badge {
    position: absolute;
    right: 10px; top: 388px;
    width: 44px; height: 44px;
    border-radius: 50%;
    background: var(--badge-orange);
    border: 2px solid #fff;
    color: #fff;
    font-weight: 700;
    font-size: 13px;
    display: flex; align-items: center; justify-content: center;
  }
  .natural-claim {
    position: absolute; left: 0; right: 0; top: 450px;
    text-align: center; color: #fff;
    font-size: 14px; letter-spacing: 2px; font-weight: 600;
  }
  .family-line {
    position: absolute; left: 0; right: 0; top: 474px;
    text-align: center; color: #fff; font-size: 11px;
  }
  .net-weight {
    position: absolute; left: 0; right: 0; top: 510px;
    text-align: center; color: #fff; font-size: 12px; letter-spacing: 1px;
  }

  .back-copy {
    position: absolute;
    left: 24px; right: 24px; top: 118px;
    color: var(--ink);
    font-size: 7.5px;
    line-height: 10px;
  }
  .back-copy .tagline {
    font-family: "Arvo", Georgia, serif;
    font-size: 10px;
    margin-bottom: 8px;
    color: var(--charcoal);
  }
  .back-copy p { margin-bottom: 8px; }
  .back-copy strong { color: var(--leaf-green); font-weight: 700; }
  .back-copy .squeeze { text-align: center; font-weight: 700; font-size: 6.5px; }
  .label-blank {
    position: absolute;
    left: 36px; top: 350px;
    width: 70px; height: 66px;
    background: #fff;
    border: 1px solid #e3e3e0;
  }
  .company-info {
    position: absolute;
    left: 150px; top: 345px;
    color: var(--leaf-green);
    font-size: 6.5px;
    line-height: 9px;
  }
</style>
</head>
<body>
  <section class="tube-panel front" aria-label="Tube front">
    <div class="brand"><span class="brand-dot"></span>Pine Hollow</div>
    <div class="front-lower"></div>
    <div class="leaf-artwork" role="img" aria-label="Soft leaf illustration in pale green behind the product name"></div>
    <h1 class="product-name">NATURAL</h1>
    <div class="product-type">TOOTHPASTE</div>
    <div class="claim-band">FLUORIDE-FREE<br>TOOTHPASTE</div>
    <div class="flavor-band">
      <div class="flavor-name">KODA FERN</div>
      <div class="flavor-label">FLAVOR</div>
    </div>
    <div class="new-badge">NEW</div>
    <div class="natural-claim">100% NATURAL</div>
    <div class="family-line">Family owned | Family approved</div>
    <div class="net-weight">4.2 FL. OZ.</div>
  </section>

  <section class="tube-panel back" aria-label="Tube back">
    <div class="brand"><span class="brand-dot"></span>Pine Hollow</div>
    <div class="back-copy">
      <div class="tagline">Naturally healthy for your family.</div>
      <p><strong>Natural Ingredients:</strong> Vegetable glycerin, De-ionized water, Xylitol, Calcium carbonate, USDA organic flavor concentrate, Sodium cocoyl sulfate derived from coconut oil, and Carrageenan (extracted from seaweed).</p>
      <p><strong>No parabens, no gluten, no glycols, no SLS, no TEA, no formaldehyde, no artificial flavors, no artificial dyes, no artificial sweetener, no dairy, no sorbitol, no saccharine, no peroxide, and no fluoride!</strong></p>
      <p><strong>Directions:</strong> Adults and children 2 years of age and older: Brush teeth thoroughly, preferably after each meal or at least twice a day or as directed by a dentist.</p>
      <p><strong>Children under 2 years:</strong> consult a dentist.</p>
      <p class="squeeze">FOR BEST RESULTS, SQUEEZE TUBE<br>FROM THE TOP DOWN.</p>
    </div>
    <div class="label-blank"></div>
    <div class="company-info">
      Pine Hollow LLC<br>
      48 Cedar Ridge Rd<br>
      Alder, OR 97000<br>
      Made in USA<br><br>
      Questions?<br>
      www.pinehollow.example<br>
      © Pine Hollow LLC
    </div>
  </section>
</body>
</html>
```